Hotel Corvani Bar Menu and Cafe Menu

I would like to Revise and Modify my existing Menu for My Hotel Corvani .1) One side is Bar Menu2) One side is Food Menu .All The Attachment has File Name to Understand Better. I have attached 3 Diff Files for Bar Menu and 3 Diff File for Food Menu which i have done in Past also i am Attaching Back ground Image i have used for the Bar Menu. also i am attaching Bar Menu New Price and Food Menu New Price which i want to Add on your New design. also i am adding some of the Food Images which i have used for Previous Designalso On Bar Menu i would like to Add some of the Images in small size Next to " Corvani Specialty Cocktails "the Images i would like too Add Next to Mighty Fine Spritzer , Marlo on Top , Copper Kite , Blue Lagoon Cocktail ETC , you don't have to add But try to Add at least 3 Images in Corvani Specialty Cocktail section. i would like to ADD on Both Menu Food and Bar Menu at the Bottom of the page i Have Address Phone number Below that i would like to Add "Open : Tuesday to Saturday From 4: 30 to 10: 30 Close : Sunday and Monday
Updates

Went on vacation/holiday

Industry/Entity Type

Hospitality

Font styles to use
Serif
Sans Serif
Decorative
Script

Requirements
Must have
• 2 Bar Menu:
• 1st one with address on the Bottom :
• Hotel Corvani
• 7413 Pellham Ave
• North Hollywood CA 91601
• Ph: 1 555 014 2297
• with Green , Chartreuse Green Black and Blue and Purple kind of Color Theme
• and
• 2nd Menu with Address :
• Hotel Corvani
• 31857 Quarrystone Ave
• Newhall , CA 91321
• with Orange , Chartreuse Green Black and Blue and Purple kind of Color Theme
• and
• Hours Open: 4:30 to 10:30 Thursday to Saturday
• Close: Sunday and Monday
• the color Theme for the 2 nd Bar menu is Orange.
Nice to have
• 2 Bar Menu:
• Hotel Corvani
• 7413 Pellham Ave
• Ph: 1 555 014 2297
• and
• 2nd Menu with Address :
• Hotel Corvani
• 31857 Quarrystone Ave
• Newhall , CA 91321
• and

```html
<!DOCTYPE html>
<html lang="en">
<head>
<meta charset="utf-8">
<title>Hotel Corvani – Cafe Food Menu</title>
<link href="https://fonts.googleapis.com/css2?family=Cagliostro&family=Roboto+Condensed:wght@400&family=Arimo:wght@400;700&display=swap" rel="stylesheet">
<style>
  :root {
    --backdrop: #ece8e1;
    --chartreuse: #b2d235;
    --title-green: #8cc63f;
    --accent-green: #7dc242;
    --rule-blue: #1d4e9e;
    --footer-black: #231f20;
    --ink: #1a1a1a;
    --white: #ffffff;
  }
  * { box-sizing: border-box; margin: 0; padding: 0; }
  html, body { width: 1200px; height: 1200px; overflow: hidden; }
  body { background: var(--backdrop); position: relative; }

  .menu-sheet {
    position: absolute; left: 158px; top: 28px;
    width: 884px; height: 1144px;
    background: var(--chartreuse);
    box-shadow: 0 4px 14px rgba(0,0,0,.25);
    overflow: hidden;
  }

  .hotel-exterior {
    position: absolute; left: 0; top: 0; width: 884px; height: 348px;
    background: linear-gradient(to bottom, #6f9fd8 0%, #a9c7ea 30%, #e6d6bd 55%, #b46a55 75%, #5f7a44 100%);
  }
  .rule { position: absolute; left: 0; width: 884px; background: var(--rule-blue); }
  .rule--top { top: 348px; height: 13px; }
  .rule--bottom { top: 929px; height: 11px; }

  .wings-photo {
    position: absolute; left: 0; top: 361px; width: 360px; height: 568px;
    background: radial-gradient(ellipse at 45% 55%, #a5581f 0%, #6e3412 45%, #3a1e10 100%);
  }

  .dish {
    position: absolute; width: 154px; height: 154px; border-radius: 50%;
    border: 3px solid var(--white);
    box-shadow: 0 2px 6px rgba(0,0,0,.35);
  }
  .dish--burger { left: 314px; top: 387px; background: radial-gradient(circle, #d18a3c 0%, #7a4a22 60%, #3b2b22 100%); }
  .dish--fish { left: 303px; top: 567px; background: radial-gradient(circle, #f1dfb0 0%, #c9b27a 45%, #4d7a3a 80%, #e8e8e8 100%); }
  .dish--pizza { left: 308px; top: 748px; background: radial-gradient(circle, #e7a34a 0%, #c4572c 55%, #8a3a22 100%); }

  .menu-heading { position: absolute; right: 39px; top: 375px; text-align: right; font-family: "Cagliostro", sans-serif; }
  .menu-heading__venue {
    font-size: 62px; line-height: 1; color: var(--title-green);
    text-shadow: 1px 2px 2px rgba(0,0,0,.35);
  }
  .menu-heading__title {
    font-size: 52px; line-height: 1.15; color: var(--white);
    text-shadow: 1px 2px 2px rgba(0,0,0,.35);
  }

  .menu-list {
    position: absolute; left: 483px; top: 586px; width: 362px;
    list-style: none;
    font-family: "Roboto Condensed", sans-serif; font-size: 16px; color: var(--ink);
  }
  .menu-item { display: flex; align-items: baseline; height: 44px; }
  .menu-item::before { content: "•"; margin-right: 5px; }
  .menu-item__name { white-space: nowrap; }
  .menu-item__leader { flex: 1; border-bottom: 1px dotted var(--ink); margin: 0 2px; transform: translateY(-4px); }
  .menu-item__price { white-space: nowrap; }

  .footer {
    position: absolute; left: 0; top: 940px; width: 884px; height: 204px;
    background: var(--footer-black);
  }
  .footer__brand {
    position: absolute; left: 32px; top: 72px;
    display: flex; align-items: center; gap: 12px;
    font-family: "Arimo", sans-serif; font-weight: 700; font-size: 40px; color: var(--white);
  }
  .footer__brand-dot { width: 16px; height: 16px; border-radius: 50%; background: var(--accent-green); }
  .footer__info { position: absolute; left: 400px; top: 10px; font-family: "Arimo", sans-serif; font-weight: 700; }
  .footer__hours { color: var(--accent-green); font-size: 25px; line-height: 36px; }
  .footer__days { color: var(--white); font-size: 25px; line-height: 36px; }
  .footer__contact { color: var(--accent-green); font-size: 31px; line-height: 44px; margin-top: 2px; }
  .footer__address { color: var(--white); font-weight: 400; font-size: 20px; line-height: 34px; }
</style>
</head>
<body>
  <main class="menu-sheet">
    <div class="hotel-exterior" role="img" aria-label="Illustrated street view of the hotel building and neighbouring shopfronts under a blue sky"></div>
    <div class="rule rule--top"></div>

    <div class="wings-photo" role="img" aria-label="Close-up photo of glazed chicken wings with a dipping sauce"></div>
    <div class="dish dish--burger" role="img" aria-label="Photo of a chicken burger"></div>
    <div class="dish dish--fish" role="img" aria-label="Photo of grilled fish fillet with lemon and greens"></div>
    <div class="dish dish--pizza" role="img" aria-label="Photo of a sliced pizza"></div>

    <header class="menu-heading">
      <h1 class="menu-heading__venue">Corvani Cafe</h1>
      <h2 class="menu-heading__title">Food Menu</h2>
    </header>

    <ul class="menu-list">
      <li class="menu-item"><span class="menu-item__name">Daily Harvest Salad ( Veggie or Chicken )</span><span class="menu-item__leader"></span><span class="menu-item__price">$8</span></li>
      <li class="menu-item"><span class="menu-item__name">Shoe Strings Fries</span><span class="menu-item__leader"></span><span class="menu-item__price">$6</span></li>
      <li class="menu-item"><span class="menu-item__name">Corvani Wings ( 7 Pieces )</span><span class="menu-item__leader"></span><span class="menu-item__price">$10</span></li>
      <li class="menu-item"><span class="menu-item__name">Sriracha Chicken Bites</span><span class="menu-item__leader"></span><span class="menu-item__price">$13</span></li>
      <li class="menu-item"><span class="menu-item__name">Chees Quesadilla ( Veggie or Chicken )</span><span class="menu-item__leader"></span><span class="menu-item__price">$9</span></li>
      <li class="menu-item"><span class="menu-item__name">Cod Fish Fillet (Craft Beer Battered with Fries )</span><span class="menu-item__leader"></span><span class="menu-item__price">$13</span></li>
      <li class="menu-item"><span class="menu-item__name">Corvani Burger ( Veggie, Chicken with Fries)</span><span class="menu-item__leader"></span><span class="menu-item__price">$13</span></li>
      <li class="menu-item"><span class="menu-item__name">Pizza (Veggie or Pepperoni )</span><span class="menu-item__leader"></span><span class="menu-item__price">$13</span></li>
    </ul>

    <div class="rule rule--bottom"></div>

    <footer class="footer">
      <div class="footer__brand"><span class="footer__brand-dot"></span>Hotel Corvani</div>
      <div class="footer__info">
        <p class="footer__hours">Hours Open: 4:30 to 10:30</p>
        <p class="footer__days">Thursday to Saturday</p>
        <p class="footer__days">Close: Sunday and Monday</p>
        <p class="footer__contact">Contact us : 1 555 014 2297</p>
        <p class="footer__address">7413 Pellham Ave, North Hollywood CA 91601</p>
      </div>
    </footer>
  </main>
</body>
</html>
```